Antiseptic products for Veloran East Africa

I need several antiseptic product designs for topical solutions such as surgical spirit, methylated spirit, hand sanitizer, calamine lotion, povidone solution, glycerine, povidone mouthwash, chlorhexidine solution, and sodium hypochlorite solution.

KINDLY START WITH THE HAND SANITIZER DESIGN, URGENT.

Target Market(s)

International market

Industry/Entity Type

Pharmaceutical

Font styles to use
Serif
Script

Colors
33a6d7
3277b5
0758a5
7651a1
886aae
e34197
e667a6
f78f20

Requirements
Must have
• Elegant designs, writtings to appear as they are. safety symbols to appear such as flammable or corrosive.
Nice to have
• Attractive colours but keep it simple and classy.

```html
<!DOCTYPE html>
<html lang="en">
<head>
<meta charset="utf-8">
<title>Clenora Advanced Hand Sanitizer Label</title>
<link href="https://fonts.googleapis.com/css2?family=Montserrat:ital,wght@0,400;0,500;0,700;0,800;1,700;1,800&family=Cormorant+Garamond:wght@500;700&display=swap" rel="stylesheet">
<style>
  :root {
    --paper: #ffffff;
    --ink: #1a1a1a;
    --brand-blue: #1b75bc;
    --deep-blue: #0758a5;
    --sky: #33a6d7;
    --mist: #93d3ef;
    --pale: #cfe9f7;
    --drop-text: #4a5fa0;
  }
  html, body {
    margin: 0;
    padding: 0;
    width: 753px;
    height: 1200px;
    overflow: hidden;
    background: var(--paper);
  }
  .label {
    display: block;
    width: 753px;
    height: 1200px;
  }
  .volume { font-family: "Montserrat", sans-serif; font-weight: 800; font-style: italic; fill: var(--paper); }
  .volume-unit { font-family: "Montserrat", sans-serif; font-weight: 400; fill: var(--paper); }
  .drop-name { font-family: "Cormorant Garamond", serif; font-weight: 500; fill: var(--drop-text); }
  .badge-text { font-family: "Montserrat", sans-serif; font-weight: 500; fill: var(--deep-blue); }
  .brand-name { font-family: "Cormorant Garamond", serif; font-weight: 700; fill: var(--paper); }
  .headline { font-family: "Montserrat", sans-serif; font-weight: 800; fill: var(--brand-blue); }
  .subline { font-family: "Montserrat", sans-serif; font-weight: 700; fill: var(--brand-blue); }
  .with { font-family: "Montserrat", sans-serif; font-weight: 400; fill: var(--brand-blue); }
  .with-strong { font-weight: 800; font-style: italic; }
</style>
</head>
<body>
<svg class="label" viewBox="0 0 1024 1632" xmlns="http://www.w3.org/2000/svg">
  <defs>
    <linearGradient id="brandOval" x1="0" y1="0" x2="0" y2="1">
      <stop offset="0" stop-color="#e6f7fd"/>
      <stop offset="0.25" stop-color="#3fc3ea"/>
      <stop offset="0.7" stop-color="#1c83cc"/>
      <stop offset="1" stop-color="#7cc3ec"/>
    </linearGradient>
    <linearGradient id="dropFill" x1="0" y1="0" x2="1" y2="1">
      <stop offset="0" stop-color="#d9f1fc"/>
      <stop offset="1" stop-color="#7dc6ec"/>
    </linearGradient>
    <linearGradient id="claimBand" x1="0" y1="0" x2="1" y2="0">
      <stop offset="0" stop-color="#ffffff" stop-opacity="0"/>
      <stop offset="0.3" stop-color="#d6eefa"/>
      <stop offset="0.8" stop-color="#d6eefa"/>
      <stop offset="1" stop-color="#ffffff" stop-opacity="0"/>
    </linearGradient>
    <radialGradient id="splashFill" cx="0.45" cy="0.6" r="0.6">
      <stop offset="0" stop-color="#f3d94a"/>
      <stop offset="0.5" stop-color="#e9e08a"/>
      <stop offset="1" stop-color="#cfe9f7" stop-opacity="0"/>
    </radialGradient>
    <path id="badgeArc" d="M 582 483 A 100 100 0 0 0 770 483"/>
  </defs>

  <!-- bottom swoosh -->
  <path class="swoosh" fill="var(--mist)" d="M 228 1452 Q 520 1490 700 1420 Q 830 1370 882 1280 Q 855 1440 710 1515 Q 540 1585 390 1545 Q 290 1515 228 1452 Z"/>

  <!-- bottle outline -->
  <path class="bottle-outline" fill="none" stroke="var(--ink)" stroke-width="3"
        d="M 520 228 C 250 300 118 700 122 1060 C 126 1400 330 1502 520 1502 C 770 1502 906 1350 906 1000 C 906 650 845 330 520 228 Z"/>

  <!-- volume banner -->
  <path class="banner-shade" fill="var(--pale)" d="M 436 250 Q 620 215 740 270 Q 840 320 880 455 Q 800 360 700 320 Q 560 265 436 250 Z"/>
  <path class="banner-mid" fill="#6fa8da" d="M 448 238 Q 630 205 750 258 Q 850 310 884 462 Q 810 345 710 300 Q 570 245 448 238 Z"/>
  <path class="banner" fill="var(--brand-blue)" d="M 462 224 Q 640 130 745 108 Q 790 104 810 160 L 886 468 Q 820 330 710 282 Q 580 228 462 224 Z"/>
  <text class="volume" x="596" y="233" font-size="50">400</text>
  <text class="volume" x="672" y="257" font-size="26">ml</text>
  <text class="volume-unit" x="718" y="258" font-size="28">e</text>

  <!-- company droplet -->
  <path class="droplet" fill="url(#dropFill)" d="M 467 360 C 480 420 532 450 532 495 C 532 532 503 557 467 557 C 431 557 403 532 403 495 C 403 450 454 420 467 360 Z"/>
  <text class="drop-name" x="467" y="497" font-size="23" text-anchor="middle">VELORAN</text>

  <!-- germ claim badge -->
  <circle cx="676" cy="447" r="68" fill="none" stroke="var(--sky)" stroke-width="15"/>
  <rect x="650" y="420" width="60" height="75" rx="20" fill="var(--sky)" role="img" aria-label="Icon of two open hands"/>
  <text class="badge-text" font-size="21" letter-spacing="1">
    <textPath href="#badgeArc" startOffset="50%" text-anchor="middle">Kills 99% of Germs</textPath>
  </text>

  <!-- brand oval -->
  <ellipse cx="509" cy="870" rx="248" ry="132" fill="url(#brandOval)"/>
  <text class="brand-name" x="509" y="900" font-size="96" text-anchor="middle">Clenora</text>

  <!-- product naming -->
  <text class="headline" x="510" y="1096" font-size="64" letter-spacing="6" text-anchor="middle">ADVANCED</text>
  <text class="subline" x="512" y="1146" font-size="40" letter-spacing="4.5" text-anchor="middle">Hand Sanitizer</text>
  <rect x="248" y="1154" width="540" height="44" fill="url(#claimBand)"/>
  <text class="with" x="512" y="1189" font-size="31" letter-spacing="3" text-anchor="middle">With <tspan class="with-strong">MOISTURIZERS</tspan></text>

  <!-- lemon splash -->
  <path class="splash" fill="url(#splashFill)" role="img" aria-label="Lemon wedge in a splash of water"
        d="M 300 1310 Q 360 1270 470 1300 Q 580 1320 640 1330 Q 700 1250 780 1160 Q 760 1300 660 1400 Q 570 1470 450 1460 Q 340 1440 300 1310 Z"/>
</svg>
</body>
</html>
```